Business card design for event company

need design double sided in square shape ( approx 6x6cm) in matt grey shades
front side :
logo ( could be in one color like picture attached ) printpress effect in a rect box

back side :
name in big font with silver foil finish ( similar to attached pic )

phone number i would like to see how it will look like if embossed ( like in credit cards )

Sample for contact on card ( will need 5 different contacts) - pls. include small icons next to each contact

KARIM SALEHI
Managing Director

+971 50 374 6619
karim@novlinkuae.com
www.novlink.ae
Building C2 , Office 318
Marsa Tirel Park

Please consider this is an urgent project . thank you in advance

```html
<!DOCTYPE html>
<html lang="en">
<head>
<meta charset="utf-8">
<title>Novlink Business Card</title>
<link rel="stylesheet" href="https://fonts.googleapis.com/css2?family=Montserrat:wght@400;500;600;700&family=Source+Sans+3:wght@500;600&display=swap">
<style>
  :root {
    --backdrop: #2f2f2f;
    --card: #e8e8e8;
    --ink: #4a4a4a;
    --ink-soft: #555555;
    --accent: #e0861c;
  }
  * { margin: 0; padding: 0; box-sizing: border-box; }
  html, body { width: 1200px; height: 900px; overflow: hidden; }
  body {
    background: var(--backdrop);
    position: relative;
    font-family: "Montserrat", sans-serif;
  }
  .card {
    position: absolute;
    top: 247px;
    width: 392px;
    height: 400px;
    background: var(--card);
  }
  .card--front { left: 176px; }
  .card--back { left: 658px; }

  .brand {
    position: absolute;
    display: flex;
    align-items: center;
    gap: 8px;
    font-family: "Montserrat", sans-serif;
    font-weight: 500;
    color: var(--ink);
    line-height: 1;
  }
  .brand__mark {
    display: block;
    background: var(--accent);
  }
  .card--front .brand { right: 24px; top: 52px; font-size: 30px; }
  .card--front .brand__mark { width: 12px; height: 12px; }
  .card--back .brand { left: 0; right: 0; top: 176px; justify-content: center; font-size: 46px; gap: 12px; }
  .card--back .brand__mark { width: 16px; height: 16px; }

  .person { position: absolute; left: 17px; top: 192px; }
  .person__name {
    font-size: 25px;
    font-weight: 500;
    color: var(--ink);
    letter-spacing: 0.2px;
    line-height: 1;
  }
  .person__name strong { font-weight: 700; }
  .person__title {
    margin-top: 10px;
    font-size: 16px;
    font-weight: 600;
    color: var(--accent);
    line-height: 1;
  }

  .contacts {
    position: absolute;
    left: 18px;
    top: 280px;
    list-style: none;
    font-family: "Source Sans 3", sans-serif;
    font-weight: 600;
    font-size: 16.5px;
    color: var(--ink-soft);
    letter-spacing: -0.2px;
  }
  .contacts__item {
    display: flex;
    align-items: center;
    height: 30px;
  }
  .contacts__icon {
    width: 16px;
    height: 16px;
    margin-right: 10px;
    flex: none;
    fill: var(--accent);
  }

  .website {
    position: absolute;
    left: 0; right: 0;
    top: 284px;
    text-align: center;
    font-family: "Montserrat", sans-serif;
    font-weight: 600;
    font-size: 13.5px;
    letter-spacing: 3px;
    color: var(--accent);
  }
</style>
</head>
<body>
  <section class="card card--front">
    <div class="brand"><span class="brand__mark"></span>Novlink</div>

    <div class="person">
      <p class="person__name"><strong>KARIM</strong> SALEHI</p>
      <p class="person__title">MANAGING DIRECTOR</p>
    </div>

    <ul class="contacts">
      <li class="contacts__item">
        <svg class="contacts__icon" viewBox="0 0 16 16" aria-hidden="true">
          <path d="M1 5.5C1 3.5 4 2.5 8 2.5s7 1 7 3v1.3h-3.2V5.2H4.2v1.6H1z"/>
          <rect x="3" y="8" width="10" height="6" rx="1"/>
        </svg>
        +971 50 374 6619
      </li>
      <li class="contacts__item">
        <svg class="contacts__icon" viewBox="0 0 16 16" aria-hidden="true">
          <path d="M1 3.5h14v9H1z M1.8 4.3 8 9l6.2-4.7" />
          <path d="M1 3.5 8 8.6l7-5.1v9H1z"/>
        </svg>
        karim@novlinkuae.com
      </li>
      <li class="contacts__item">
        <svg class="contacts__icon" viewBox="0 0 16 16" aria-hidden="true">
          <path d="M8 1a5 5 0 0 0-5 5c0 3.6 5 9 5 9s5-5.4 5-9a5 5 0 0 0-5-5zm0 7a2 2 0 1 1 0-4 2 2 0 0 1 0 4z"/>
        </svg>
        Building C2 , Office 318, Marsa Tirel Park
      </li>
    </ul>
  </section>

  <section class="card card--back">
    <div class="brand"><span class="brand__mark"></span>Novlink</div>
    <p class="website">www.novlink.ae</p>
  </section>
</body>
</html>
```